Email Signature Design

Please design an email signature, the below is an example of our current design;
___

CARVANE ESTATE HOLDINGS PTY LTD
BENEDICT ORSMAN
Licensed Strata and Community Manager

164 Galloway Lane,
ULTIMO NSW 2007

P: 02.9735.6208 F: 9640.3372
Website: www.carvaneestate.com.au

This e-mail message and accompanying data may contain information that is confidential and private. If you are not the intended recipient, the use, dissemination, distribution or copying of this message or data is prohibited.

If you have received this e-mail in error please notify us immediately and delete all material pertaining to this e-mail. strata@carvaneestate.com.au

___

We would like to incorporate our logo and company colours, you can view the colours and feel of image at www.carvaneestate.com.au

Industry/Entity Type

It Company

Requirements
Must have
• use of logo and company colours (image)

```html
<!DOCTYPE html>
<html lang="en">
<head>
<meta charset="utf-8">
<title>Email Signature – Carvane Estate Holdings</title>
<link rel="stylesheet" href="https://fonts.googleapis.com/css2?family=Arimo:wght@400;700&display=swap">
<style>
  :root {
    --olive: #7d7b3c;
    --sand: #e1d4ab;
    --slate: #6f6f6f;
    --ink: #1f1f1f;
    --paper: #ffffff;
  }
  html, body {
    margin: 0;
    padding: 0;
    width: 1200px;
    height: 281px;
    overflow: hidden;
    background: var(--paper);
  }
  .signature {
    position: relative;
    width: 1200px;
    height: 281px;
    font-family: "Arimo", Arial, sans-serif;
    color: var(--ink);
  }
  .brand {
    position: absolute;
    left: 74px;
    top: 70px;
    display: flex;
    align-items: center;
    gap: 10px;
  }
  .brand-square {
    width: 34px;
    height: 34px;
    background: var(--olive);
  }
  .brand-name {
    font-size: 14px;
    font-weight: 700;
    color: var(--olive);
    letter-spacing: 0.2px;
  }
  .tagline {
    position: absolute;
    left: 74px;
    top: 133px;
    font-size: 11px;
    color: var(--slate);
    letter-spacing: 0.2px;
  }
  .person-name {
    position: absolute;
    left: 74px;
    top: 158px;
    font-size: 13px;
    font-weight: 700;
    color: var(--olive);
    margin: 0;
  }
  .contact-line {
    position: absolute;
    left: 74px;
    top: 180px;
    display: flex;
    align-items: center;
    font-size: 14px;
    white-space: nowrap;
  }
  .divider {
    color: var(--slate);
    margin: 0 12px;
  }
  .contact-icon {
    display: inline-flex;
    align-items: center;
    justify-content: center;
    width: 16px;
    height: 16px;
    border-radius: 50%;
    background: var(--olive);
    color: var(--paper);
    font-size: 10px;
    margin: 0 6px 0 4px;
  }
  .contact-gap { margin-right: 8px; }
  .rule {
    position: absolute;
    left: 67px;
    top: 203px;
    width: 1053px;
    height: 4px;
    display: flex;
  }
  .rule span { flex: 1; }
  .rule .sand { background: var(--sand); }
  .rule .olive { background: var(--olive); }
  .rule .slate { background: var(--slate); }
  .disclaimer {
    position: absolute;
    left: 67px;
    top: 210px;
    width: 1070px;
    margin: 0;
    font-size: 10.4px;
    line-height: 17px;
    color: var(--ink);
  }
</style>
</head>
<body>
  <div class="signature">
    <div class="brand">
      <div class="brand-square"></div>
      <div class="brand-name">CARVANE ESTATE HOLDINGS</div>
    </div>
    <div class="tagline">STRATA MANAGEMENT SERVICES</div>

    <h1 class="person-name">BENEDICT ORSMAN</h1>

    <div class="contact-line">
      <span>Licensed Strata and Community Manager</span>
      <span class="divider">|</span>
      <span>164 Galloway Lane, ULTIMO NSW 2007</span>
      <span class="divider">|</span>
      <span class="contact-icon">P</span><span class="contact-gap">02.9735.6208</span>
      <span class="contact-icon">F</span><span class="contact-gap">9640.3372</span>
      <span class="contact-icon">W</span><span>www.carvaneestate.com.au</span>
    </div>

    <div class="rule">
      <span class="sand"></span>
      <span class="olive"></span>
      <span class="slate"></span>
    </div>

    <p class="disclaimer">This e-mail message and accompanying data may contain information that is confidential and private. If you are not the intended recipient, the use, dissemination, distribution or copying of this message or data is prohibited.<br>If you have received this e-mail in error please notify us immediately and delete all material pertaining to this e-mail. strata@carvaneestate.com.au</p>
  </div>
</body>
</html>
```